design packaging for adult diapers

Introduction

We are a business offering adult diapers to disabled and elderly people.
We are looking to get a design template to suit our range of adult diapers

They will be in different Models (Pull ups and wrap arounds)
3 different sizes (S/M, M/L , L/XL)
Different Types (standard absorbency, and high absorbency)

Included is the following

Design template
Brand Logo (Lumora)
Include the word “Professional” somewhere on the packaging

General Information
Type:
Size
No. of pieces
Size chart
M/L -
All products are Unisex (maybe have a logo for that?)
Absorbency Rates would be different (Standard Vs High)
Include area in design to convey the absorbency with description.

General features of the Diaper (maybe use icons?)
- Breathable material
- Extra soft
- Elastic Waist
- Super Absorbent
- Re - Stickable tapes (for wrap around type)
- Leakage barrier

Pull Ups Features:
Gentle and skin-sensitive surface layer utilizing hot air technology.
An innovation 3D Diversion layer enhances absorption speed
Advanced liquid locking technology for execptional efficiency
Permeable Film Technology
360 Degree fully elasticated waistband for a snug and comfortable fit
Combination of a leakproof waistline and elasticised leg holes

Wrap Around Features
Ensuring prolonged dryness for nighttime use and efficient mass absorption.
The dual cotton core delivers dryness and comfort.
non-woven breathable film allows for unrestricted airflow, promoting breathability
The elastic waistline with leakproof edges offers a secure and reliable fit
Premium quality waist band for a custom fit
The wetness indicator conveniently fades when the diaper is wet, making it practical for caregivers and nursing.

Manufacturer product information
- Made By Tarvely Health
- Warehouse: 7/14 Marlow Avenue Condell NSW 2167
- Ph: 0411 382 579
- www.lumorahealthcare.com.au
- An Proudly Australian owned business
Updates

Target Market(s)

adults, disabled people, elderly people,

Industry/Entity Type

healthcare

Requirements
Must have
• include "Professional" in the packaging
Nice to have
• nice to have some icons/mini illustrations next to features
Should not have
• Should not have pictures of people on the packaging

```html
<!DOCTYPE html>
<html lang="en">
<head>
<meta charset="utf-8">
<title>Lumora Professional Overnight Pull-Ups – L/XL Carton</title>
<link href="https://fonts.googleapis.com/css2?family=Roboto:ital,wght@0,400;0,500;0,700;1,400&display=swap" rel="stylesheet">
<style>
:root{
  --navy:#262a78;
  --navy-deep:#1e2160;
  --blue:#2f5aa8;
  --magenta:#b3197d;
  --magenta-bright:#d21f8f;
  --yellow:#e4ea3c;
  --orange:#f0a21c;
  --teal:#3f8893;
  --white:#ffffff;
  --ink:#1c1f4a;
  --stage:#111114;
}
*{box-sizing:border-box;margin:0;padding:0}
html,body{width:892px;height:1200px;overflow:hidden;background:var(--stage)}
body{font-family:"Roboto",sans-serif;color:var(--white);position:relative}

.dieline{position:absolute;left:0;top:313px;width:892px;height:573px}
.panel{position:absolute;overflow:hidden}
.panel--flap{left:223px;top:0;width:446px;height:147px;
  background:radial-gradient(ellipse at 20% 40%,var(--blue),var(--navy) 70%)}
.panel--left{left:0;top:147px;width:223px;height:279px;
  background:radial-gradient(ellipse at 30% 50%,#2d4c9e,var(--navy) 75%)}
.panel--front{left:223px;top:147px;width:446px;height:279px;
  background:radial-gradient(ellipse at 30% 55%,#2d56a6,var(--navy) 70%)}
.panel--right{left:669px;top:147px;width:223px;height:279px;background:var(--navy)}
.panel--base{left:223px;top:426px;width:446px;height:147px;
  background:radial-gradient(ellipse at 40% 20%,#2b4fa0,var(--navy) 75%)}

.wave-texture{position:absolute;inset:0;
  background:linear-gradient(160deg,transparent 40%,rgba(120,150,230,.18) 55%,transparent 70%)}

.product-visual{position:absolute;left:5px;top:36px;width:198px;height:198px;border-radius:50%;
  background:radial-gradient(circle at 50% 45%,#f4f5f8 0 38%,#9fb4dc 52%,rgba(47,90,168,.5) 66%,rgba(38,42,120,0) 72%)}
.arc-caption{position:absolute;left:5px;top:36px;width:198px;height:198px}

.range-label{position:absolute;font-size:7px;font-weight:500;letter-spacing:3px;color:#dfe5f7;line-height:1}
.panel--front .range-label{left:183px;top:26px}
.panel--base .range-label{left:45px;top:14px;font-size:6px;letter-spacing:2.4px}

.brand-name{position:absolute;font-weight:700;color:#f1f4fb;letter-spacing:.5px;line-height:1}
.panel--front .brand-name{left:178px;top:40px;font-size:46px}
.panel--base .brand-name{left:42px;top:25px;font-size:33px}

.tagline-band{position:absolute;background:var(--magenta);transform:skewX(-12deg);
  display:flex;align-items:center;justify-content:center}
.tagline-band span{transform:skewX(12deg);font-style:italic;color:#fff;white-space:nowrap}
.panel--front .tagline-band{left:168px;top:95px;width:180px;height:20px}
.panel--front .tagline-band span{font-size:12px}
.panel--base .tagline-band{left:38px;top:62px;width:104px;height:11px}
.panel--base .tagline-band span{font-size:7px}

.product-title{position:absolute;text-align:center;line-height:1}
.product-title .overline{font-weight:500;letter-spacing:.3px}
.product-title .main{font-weight:700;color:var(--yellow);letter-spacing:.3px}
.product-title .audience{font-weight:400}
.product-title .audience em{font-style:normal;color:var(--magenta-bright)}
.panel--front .product-title{left:190px;top:133px;width:120px}
.panel--front .overline{font-size:13px}
.panel--front .main{font-size:21px}
.panel--front .audience{font-size:7.5px;margin-top:1px}
.panel--base .product-title{left:172px;top:46px;width:118px}
.panel--base .overline{font-size:12px}
.panel--base .main{font-size:19px}
.panel--base .audience{font-size:7px;margin-top:1px}

.size-tag{position:absolute;left:355px;top:0;width:56px;height:161px;text-align:center;color:var(--ink);
  background:var(--yellow);border-radius:0 0 4px 4px;box-shadow:2px 2px 0 var(--orange);line-height:1}
.size-tag__head{background:var(--magenta);color:#fff;height:50px;padding-top:9px;font-weight:500;
  border-radius:0 0 6px 6px}
.size-tag__head .fit{font-size:14px;font-weight:700}
.size-tag__head .age{font-size:13px}
.size-tag__body{padding-top:5px}
.size-tag .label{font-size:11px;font-weight:700}
.size-tag .small{font-size:7px;font-weight:700}
.size-tag .range{font-size:12px;font-weight:700}
.size-tag .range--mm{font-size:9px}
.size-tag hr{border:0;border-top:1px solid var(--ink);width:36px;margin:3px auto}
.size-tag .count{font-size:14px;font-weight:700}
.size-tag .desc{font-size:5.5px;font-weight:500;line-height:1.2}

.unisex-note{position:absolute;left:355px;top:171px;width:56px;text-align:center;font-size:5.5px;font-weight:700;line-height:1.2}
.unisex-mark{display:block;width:9px;height:9px;margin:0 auto 3px;border-radius:50%;background:#fff}

.seal{position:absolute;border-radius:50%;background:#dfe6f5;border:2px solid #5d78b9;box-shadow:0 0 0 1.5px #fff}

/* absorbency box: all inner sizes in em of the box font-size */
.absorbency{position:absolute;background:#fff;border-radius:.35em;color:var(--ink);overflow:hidden;
  width:11.3em;height:3.9em;line-height:1}
.absorbency .upto{position:absolute;left:.9em;top:.35em;font-size:.8em;font-weight:500}
.absorbency .rule{position:absolute;left:3.5em;top:.72em;width:3em;height:.12em;background:var(--ink)}
.absorbency .hours{position:absolute;left:.9em;top:1.2em;font-size:1.3em;font-weight:500;white-space:nowrap}
.absorbency .hours small{font-size:.26em;display:inline-block;line-height:1.15;vertical-align:middle;margin-left:.2em;font-weight:400}
.absorbency .drops{position:absolute;left:7em;top:.4em;width:4em;height:1.7em}
.absorbency .strip{position:absolute;left:1.45em;right:1.45em;bottom:0;font-size:.42em;height:2.7em;line-height:2.7em;
  background:var(--navy);border-radius:.7em .7em 0 0;color:#fff;text-align:center;white-space:nowrap}
.panel--front .absorbency{left:283px;top:200px;font-size:10px}
.panel--base .absorbency{left:22px;top:76px;font-size:11.4px}

.disclaimer{position:absolute;left:28px;top:259px;font-size:5.4px;color:#e6e9f6}

.feature-list{position:absolute;left:49px;top:25px;list-style:none;font-size:8.4px;line-height:1.4;color:#fff}
.icon-grid{position:absolute;left:22px;top:116px;width:178px;height:136px;background:#fff;
  display:grid;grid-template-columns:repeat(4,1fr);grid-template-rows:repeat(4,1fr);place-items:center;padding:4px}
.icon-grid svg{width:26px;height:24px}

.maker-info{position:absolute;left:307px;top:45px;font-size:6.6px;line-height:1.33;color:#fff}
.maker-info strong{font-weight:700;display:block}
</style>
</head>
<body>
<main class="dieline" aria-label="Lumora professional overnight pull-ups carton dieline">

  <section class="panel panel--flap"><div class="wave-texture"></div></section>
  <section class="panel panel--left"><div class="wave-texture"></div></section>

  <section class="panel panel--front">
    <div class="wave-texture"></div>
    <div class="product-visual" role="img" aria-label="Illustration of a white pull-up adult diaper inside a glowing blue ring"></div>
    <svg class="arc-caption" viewBox="0 0 198 198">
      <defs><path id="captionArc" d="M40 150 A80 80 0 0 0 160 150"/></defs>
      <text font-family="Roboto, sans-serif" font-size="9.5" fill="#fff" text-anchor="middle">
        <textPath href="#captionArc" startOffset="50%">Easy Fit &amp; Comfortable</textPath>
      </text>
    </svg>

    <div class="range-label">PROFESSIONAL</div>
    <div class="brand-name">Lumora</div>
    <div class="tagline-band"><span>Premium Adult Dry Pants</span></div>
    <div class="product-title">
      <div class="overline">OVERNIGHT</div>
      <div class="main">PULL-UPS</div>
      <div class="audience">— FOR MEN &amp; <em>WOMEN</em> —</div>
    </div>

    <div class="size-tag">
      <div class="size-tag__head"><div class="fit">L/XL</div><div class="age">Adult</div></div>
      <div class="size-tag__body">
        <div class="label">SIZE</div>
        <div class="small">WAIST</div>
        <div class="range">34-59</div>
        <div class="small">INCHES</div>
        <hr>
        <div class="range range--mm">863-1500</div>
        <div class="small">MM</div>
        <hr>
        <div class="count">10</div>
        <div class="desc">Disposable<br>Adult Dry Pants</div>
      </div>
    </div>

    <div class="unisex-note"><span class="unisex-mark"></span>UNISEX ADULT<br>DIAPERS</div>

    <div class="seal" style="left:187px;top:214px;width:34px;height:34px"></div>
    <div class="seal" style="left:232px;top:214px;width:34px;height:34px"></div>

    <div class="absorbency">
      <span class="upto">UPTO</span><span class="rule"></span>
      <span class="hours">12-16<small>Hours<br>Protection</small></span>
      <svg class="drops" viewBox="0 0 52 22">
        <defs><path id="dropA" d="M4 0C4 0 0 5 0 7.5a4 4 0 0 0 8 0C8 5 4 0 4 0Z"/></defs>
        <g fill="#2a2f86">
          <use href="#dropA" x="2" y="0"/><use href="#dropA" x="12" y="0"/><use href="#dropA" x="22" y="0"/><use href="#dropA" x="32" y="0"/><use href="#dropA" x="42" y="0"/>
          <use href="#dropA" x="2" y="11"/><use href="#dropA" x="12" y="11"/><use href="#dropA" x="22" y="11"/>
        </g>
        <g fill="none" stroke="#2a2f86" stroke-width=".8"><use href="#dropA" x="32" y="11"/><use href="#dropA" x="42" y="11"/></g>
      </svg>
      <span class="strip">standard absorbency and high absorbency</span>
    </div>

    <p class="disclaimer">The diaper images shown above are only for graphical representation, actual product may differ</p>
  </section>

  <section class="panel panel--right">
    <ul class="feature-list">
      <li>- BREATHABLE MATERIAL</li>
      <li>- EXTRA SOFT</li>
      <li>- ELASTIC WAIST</li>
      <li>- SUPER ABSORBENT</li>
      <li>- RE - STICKABLE TAPES</li>
      <li>&nbsp;&nbsp;(FOR WRAP AROUND TYPE)</li>
      <li>- LEAKAGE BARRIER</li>
    </ul>
    <div class="icon-grid" role="img" aria-label="Sixteen teal feature icons">
      <svg viewBox="0 0 26 24"><path d="M3 12h20M13 2v7M10 6l3 3 3-3M13 22v-7M10 18l3-3 3 3" stroke="#3f8893" stroke-width="1.4" fill="none"/></svg>
      <svg viewBox="0 0 26 24"><path d="M3 18q10-8 20 0z" fill="#3f8893"/><path d="M13 4c0 0-3 4-3 6a3 3 0 0 0 6 0c0-2-3-6-3-6z" fill="#3f8893"/></svg>
      <svg viewBox="0 0 26 24"><circle cx="13" cy="12" r="10" fill="#3f8893"/><path d="M6 5l14 14" stroke="#fff" stroke-width="1.6"/></svg>
      <svg viewBox="0 0 26 24"><path d="M3 8q10-6 20 0v8q-10 6-20 0z" fill="#3f8893"/><circle cx="13" cy="9" r="3" fill="#fff"/></svg>
      <svg viewBox="0 0 26 24"><path d="M4 20Q4 6 20 4Q22 18 4 20z" fill="none" stroke="#3f8893" stroke-width="1.6"/></svg>
      <svg viewBox="0 0 26 24"><circle cx="9" cy="11" r="6" fill="#3f8893"/><circle cx="18" cy="11" r="6" fill="none" stroke="#3f8893" stroke-width="1.4"/></svg>
      <svg viewBox="0 0 26 24"><circle cx="13" cy="13" r="9" fill="#3f8893"/><rect x="10" y="2" width="6" height="4" fill="#3f8893"/></svg>
      <svg viewBox="0 0 26 24"><path d="M3 18q10-10 20 0z" fill="#3f8893"/><path d="M6 12l7-6 7 6" stroke="#3f8893" stroke-width="1.4" fill="none"/></svg>
      <svg viewBox="0 0 26 24"><path d="M4 16h18v4H4z" fill="#3f8893"/><path d="M13 14V3M9 7l4-4 4 4" stroke="#3f8893" stroke-width="1.6" fill="none"/></svg>
      <svg viewBox="0 0 26 24"><path d="M13 2Q4 12 13 22Q22 12 13 2z" fill="none" stroke="#3f8893" stroke-width="1.4"/></svg>
      <svg viewBox="0 0 26 24"><path d="M3 6h20l-4 14H7z" fill="#3f8893"/></svg>
      <svg viewBox="0 0 26 24"><path d="M3 5h20v6q-10 12-20 0z" fill="none" stroke="#3f8893" stroke-width="1.6"/></svg>
      <svg viewBox="0 0 26 24"><circle cx="13" cy="11" r="9" fill="#3f8893"/><path d="M4 20h18" stroke="#3f8893" stroke-width="1.6"/></svg>
      <svg viewBox="0 0 26 24"><rect x="5" y="3" width="16" height="5" rx="2" fill="none" stroke="#3f8893" stroke-width="1.3"/><rect x="5" y="10" width="16" height="5" rx="2" fill="none" stroke="#3f8893" stroke-width="1.3"/><rect x="5" y="17" width="16" height="5" rx="2" fill="none" stroke="#3f8893" stroke-width="1.3"/></svg>
      <svg viewBox="0 0 26 24"><path d="M3 16q10-10 20 0v3H3z" fill="#3f8893"/></svg>
      <svg viewBox="0 0 26 24"><circle cx="12" cy="14" r="8" fill="#3f8893"/><path d="M18 4l4 3" stroke="#3f8893" stroke-width="1.6"/></svg>
    </div>
  </section>

  <section class="panel panel--base">
    <div class="wave-texture"></div>
    <div class="range-label">PROFESSIONAL</div>
    <div class="brand-name">Lumora</div>
    <div class="tagline-band"><span>Premium Adult Dry Pants</span></div>
    <div class="absorbency">
      <span class="upto">UPTO</span><span class="rule"></span>
      <span class="hours">12-16<small>Hours<br>Protection</small></span>
      <svg class="drops" viewBox="0 0 52 22">
        <defs><path id="dropB" d="M4 0C4 0 0 5 0 7.5a4 4 0 0 0 8 0C8 5 4 0 4 0Z"/></defs>
        <g fill="#2a2f86">
          <use href="#dropB" x="2" y="0"/><use href="#dropB" x="12" y="0"/><use href="#dropB" x="22" y="0"/><use href="#dropB" x="32" y="0"/><use href="#dropB" x="42" y="0"/>
          <use href="#dropB" x="2" y="11"/><use href="#dropB" x="12" y="11"/><use href="#dropB" x="22" y="11"/>
        </g>
        <g fill="none" stroke="#2a2f86" stroke-width=".8"><use href="#dropB" x="32" y="11"/><use href="#dropB" x="42" y="11"/></g>
      </svg>
      <span class="strip">standard absorbency and high absorbency</span>
    </div>
    <div class="product-title">
      <div class="overline">OVERNIGHT</div>
      <div class="main">PULL-UPS</div>
      <div class="audience">— FOR MEN &amp; <em>WOMEN</em> —</div>
    </div>
    <div class="seal" style="left:201px;top:93px;width:27px;height:27px"></div>
    <div class="seal" style="left:236px;top:93px;width:27px;height:27px"></div>
    <div class="maker-info">
      <strong>MANUFACTURER PRODUCT<br>INFORMATION</strong>
      Made By Tarvely Health<br>
      Warehouse: 7/14 Marlow Avenue<br>
      Condell NSW 2167<br>
      Ph: 0411 382 579<br>
      www.lumorahealthcare.com.au<br>
      An Proudly Australian owned business
    </div>
  </section>

</main>
</body>
</html>
```